Commercial Loan Originator Business Card (CHANGE COLORS SCHEME)

CHANGE COLOR SCHEME - SAME DESIGN

Name Marissa Lantham
Title Commercial Loan Originator
Office (800) 641-2905 x68
Direct (240) 617-2435
Email brightleaf4you@mailpost.example

Name Derek Fallow
Office (800) 641-2905 x70
Direct (410) 932-1864
Email d.falthebroker@mailpost.example

Name Gordon Wexley
Office (800) 641-2905 x71
Direct (215) 346-2081
Email g.wexley37@mailpost.example

Name Lyn Moreau
Office (800) 641-2905 x
Direct (202) 458-1937
Email lmoreau64@mailpost.example

Name Nadia Strand
Office (800) 641-2905 x72
Direct (240) 871-5246
Email qrzhomelending@mailpost.example

```html
<!DOCTYPE html>
<html lang="en">
<head>
<meta charset="utf-8">
<title>Lyn Moreau – Business Card</title>
<link rel="stylesheet" href="https://fonts.googleapis.com/css2?family=Montserrat:wght@400;500;800&display=swap">
<style>
  :root {
    --stage: #e4e5e8;
    --card: #ffffff;
    --navy: #1f2f7a;
    --ink: #1c1c24;
    --portrait-a: #3a2a26;
    --portrait-b: #6b4a3e;
    --portrait-c: #7d3a78;
    --portrait-d: #5b6aa8;
  }
  * { box-sizing: border-box; margin: 0; padding: 0; }
  html, body {
    width: 1200px; height: 788px; overflow: hidden;
    background: var(--stage);
    font-family: "Montserrat", sans-serif;
  }
  .business-card {
    position: absolute;
    left: 100px; top: 108px;
    width: 1000px; height: 572px;
    background: var(--card);
    border-radius: 34px;
    border-left: 5px solid var(--navy);
    border-bottom: 7px solid var(--navy);
    overflow: hidden;
    box-shadow: 0 18px 40px rgba(0,0,0,.18);
  }
  .identity {
    position: absolute;
    left: 66px; top: 258px;
  }
  .identity__name {
    font-weight: 800;
    font-size: 44px;
    letter-spacing: 1px;
    color: var(--navy);
    line-height: 1.05;
    text-transform: uppercase;
  }
  .identity__title {
    font-weight: 400;
    font-size: 23px;
    letter-spacing: .8px;
    color: var(--ink);
    margin-top: 4px;
  }
  .identity__rule {
    width: 22px; height: 2px;
    background: var(--navy);
    margin: 26px 0 22px;
  }
  .contact-list { list-style: none; }
  .contact-list__item {
    display: flex; align-items: center; gap: 14px;
    font-size: 24px; font-weight: 400;
    color: var(--ink);
    letter-spacing: .6px;
    margin-bottom: 12px;
  }
  .contact-list__icon { width: 22px; height: 22px; flex: none; }
  .portrait {
    position: absolute;
    right: 0; bottom: 0;
    width: 400px; height: 470px;
    border-top-left-radius: 180px 200px;
    background:
      radial-gradient(ellipse 45% 35% at 55% 30%, var(--portrait-b), transparent 70%),
      linear-gradient(170deg, var(--portrait-a) 0%, var(--portrait-a) 45%, var(--portrait-c) 70%, var(--portrait-d) 100%);
  }
</style>
</head>
<body>
  <div class="business-card">
    <div class="identity">
      <h1 class="identity__name">Lyn Moreau</h1>
      <p class="identity__title">Commercial Loan Originator</p>
      <div class="identity__rule"></div>
      <ul class="contact-list">
        <li class="contact-list__item">
          <svg class="contact-list__icon" viewBox="0 0 24 24" aria-hidden="true"><path fill="#1f2f7a" d="M6.6 10.8a15 15 0 0 0 6.6 6.6l2.2-2.2a1 1 0 0 1 1-.25 11.4 11.4 0 0 0 3.6.57 1 1 0 0 1 1 1V20a1 1 0 0 1-1 1A17 17 0 0 1 3 4a1 1 0 0 1 1-1h3.5a1 1 0 0 1 1 1c0 1.25.2 2.45.57 3.57a1 1 0 0 1-.25 1z"/></svg>
          <span>(800) 641-2905 x</span>
        </li>
        <li class="contact-list__item">
          <svg class="contact-list__icon" viewBox="0 0 24 24" aria-hidden="true"><rect x="6" y="2" width="12" height="20" rx="2" fill="none" stroke="#1f2f7a" stroke-width="2"/><circle cx="12" cy="18" r="1.2" fill="#1f2f7a"/></svg>
          <span>(202) 458-1937</span>
        </li>
        <li class="contact-list__item">
          <svg class="contact-list__icon" viewBox="0 0 24 24" aria-hidden="true"><rect x="2" y="5" width="20" height="14" rx="1" fill="#1f2f7a"/><path d="M2 6l10 7 10-7" fill="none" stroke="#fff" stroke-width="1.6"/></svg>
          <span>lmoreau64@mailpost.example</span>
        </li>
      </ul>
    </div>
    <div class="portrait" role="img" aria-label="Smiling portrait photo of Lyn Moreau wearing glasses and a patterned purple and blue top"></div>
  </div>
</body>
</html>
```